Certificate Design for Employee Loyalty

We're a digital marketing agency in Australia (www.tidewavestudio.com.au) and we're looking to create a design for a certificate to celebrate employees who reach 5 years with us (we have a few coming up soon).
Ideally we'd want something that captures our funky, digital agency culture (see our Chatterloop page www.chatterloop.net/tidewavestudio for what we mean) and not be too "corporatey"
A4 portrait or landscape designs would be awesome, with spots for employee's name, a brief 2-3 line message and a design that reflects our culture and the 5 year milestone for the employee.
Any questions, please post!
Digital marketing employees.
Landscape

```html
<!DOCTYPE html>
<html lang="en">
<head>
<meta charset="utf-8">
<title>Tidewave Studio – Loyalty Award Certificate</title>
<link rel="stylesheet" href="https://fonts.googleapis.com/css2?family=Kaushan+Script&family=Oswald:wght@300;400&family=Questrial&family=Allura&display=swap">
<style>
  :root {
    --ink: #2b2b2b;
    --ink-soft: #555555;
    --rule: #9a9a9a;
    --paper: #ffffff;
    --frame: #333333;
    --accent: #2f8fc6;
    --art-fill: #ececec;
  }
  * { box-sizing: border-box; margin: 0; padding: 0; }
  html, body {
    width: 1200px; height: 849px; overflow: hidden;
    background: var(--paper);
  }
  .certificate {
    position: relative; width: 1200px; height: 849px;
    background: var(--paper); color: var(--ink);
    font-family: "Questrial", sans-serif;
  }
  .frame-outer {
    position: absolute; left: 26px; top: 26px; width: 1148px; height: 796px;
    border: 12px solid var(--frame);
  }
  .frame-inner {
    position: absolute; left: 44px; top: 44px; width: 1112px; height: 760px;
    border: 1.5px solid var(--frame);
  }
  .brand {
    position: absolute; top: 62px; left: 0; width: 1200px;
    display: flex; justify-content: center; align-items: center; gap: 10px;
    font-family: "Questrial", sans-serif; font-size: 30px; color: var(--ink-soft);
    letter-spacing: 1px;
  }
  .brand-dot { width: 18px; height: 18px; border-radius: 50%; background: var(--accent); }
  .title-arc { position: absolute; left: 0; top: 0; width: 1200px; height: 849px; }
  .title-arc text {
    font-family: "Kaushan Script", cursive; font-size: 64px; fill: var(--ink);
  }
  .awarded-to {
    position: absolute; top: 220px; left: 0; width: 1200px;
    display: flex; justify-content: center; align-items: center; gap: 14px;
    font-size: 17px; color: var(--ink-soft); letter-spacing: 0.5px;
  }
  .awarded-to .dash { width: 46px; height: 1px; background: var(--ink-soft); }
  .art {
    position: absolute; background: var(--art-fill); border-radius: 6px;
  }
  .art-pair { left: 553px; top: 248px; width: 94px; height: 80px; }
  .art-left { left: 241px; top: 502px; width: 138px; height: 118px; }
  .art-right { left: 830px; top: 502px; width: 138px; height: 118px; }
  .recipient {
    position: absolute; top: 330px; left: 338px; width: 554px; height: 100px;
    border-bottom: 1.5px solid var(--ink-soft);
    text-align: center;
    font-family: "Kaushan Script", cursive; font-size: 78px; line-height: 96px;
    color: var(--ink);
  }
  .message {
    position: absolute; top: 436px; left: 446px; width: 318px;
    text-align: center; font-family: "Oswald", sans-serif; font-weight: 300;
    font-size: 22px; line-height: 38px; color: var(--ink);
    text-transform: uppercase; letter-spacing: 0.3px;
    border-bottom: 1px solid #cfcfcf; padding-bottom: 2px;
  }
  .date-badge {
    position: absolute; top: 522px; left: 548px; width: 94px;
    text-align: center; color: var(--ink);
  }
  .date-badge .given {
    display: block; font-family: "Oswald", sans-serif; font-weight: 400;
    font-size: 12px; text-transform: uppercase; letter-spacing: 0.5px;
    border-top: 1px solid var(--ink-soft); border-bottom: 1px solid var(--ink-soft);
    margin: 0 6px; line-height: 16px;
  }
  .date-badge .day {
    display: block; font-family: "Allura", cursive; font-size: 18px; line-height: 22px;
  }
  .date-badge .month {
    display: block; font-family: "Oswald", sans-serif; font-weight: 400;
    font-size: 40px; line-height: 40px;
  }
  .date-badge .year {
    display: block; font-family: "Oswald", sans-serif; font-weight: 300;
    font-size: 20px; letter-spacing: 2px; line-height: 24px;
    border-bottom: 1px solid var(--ink-soft); margin: 0 10px;
  }
  .signature {
    position: absolute; top: 688px; left: 461px; width: 284px;
    text-align: center;
  }
  .signature .sign-mark {
    display: block; font-family: "Allura", cursive; font-size: 44px; line-height: 58px;
    color: var(--ink); border-bottom: 1.5px solid var(--ink-soft);
  }
  .signature .sign-label {
    display: block; font-size: 16px; color: var(--ink-soft); margin-top: 4px;
  }
</style>
</head>
<body>
<main class="certificate">
  <div class="frame-outer"></div>
  <div class="frame-inner"></div>

  <header class="brand">
    <span>Tidewave Studio</span><span class="brand-dot"></span>
  </header>

  <svg class="title-arc" viewBox="0 0 1200 849" aria-label="Loyalty Award Certificate">
    <defs><path id="title-curve" d="M190,240 Q600,138 1012,240"/></defs>
    <text><textPath href="#title-curve" startOffset="50%" text-anchor="middle">Loyalty Award Certificate</textPath></text>
  </svg>

  <p class="awarded-to"><span class="dash"></span>is hereby awarded to<span class="dash"></span></p>

  <div class="art art-pair" role="img" aria-label="Sketch of two colleagues working together at a laptop"></div>

  <h1 class="recipient">Sam Delaney</h1>

  <p class="message">In grateful appreciation of your<br>5 years of outstanding loyalty</p>

  <div class="art art-left" role="img" aria-label="Sketch of a staff member typing at a desktop computer"></div>
  <div class="art art-right" role="img" aria-label="Sketch of a staff member typing at a desktop computer"></div>

  <div class="date-badge">
    <span class="given">Given this</span>
    <span class="day">31st day of</span>
    <span class="month">MAY</span>
    <span class="year">2014</span>
  </div>

  <div class="signature">
    <span class="sign-mark">Signature</span>
    <span class="sign-label">Signature</span>
  </div>
</main>
</body>
</html>
```